Cookie Cutter Company Looking for Packaging Design

Our Company name is "dottyfaze baking co." and we are a new baking company that creates emoji style cookie cutters.

We need packaging design for 2 different packages:
Package 1: used to package 1 cookie cutter. Dieline with dimensions can be found in the "1-Pack Dieline" attachment
Package 2: used to package 3 cookie cutters. Dieline with dimensions can be found in the "3-Pack Dieline" attachment

We are looking for a simple, industrial yet catchy design that integrates our company name, company logo, and uses cardboard like color for the majority of the box. The packaging will be a window box to show the product. The product itself will be red made out of plastic. Company name, logo, and product images are attached.

Once complete, we should be able to hand the final files to a packaging manufacturer in China so that they could manufacture the packaging for us

Industry/Entity Type

Requirements
Must have
• 1) the correct files and format to give a packaging manufacturer to make us the packaging
• 2) packaging should have company name/logo
• 3) packaging should have a window box
• 4) since we will have many different cookie cutter styles and each of them will have their own title, we would you be able to add a title to the front of the box (i.e. Smile Face Cookie Cutter). This allows customers to see what cookie cutter they are purchasing.
Nice to have
• packaging should have the recipe on the back

```html
<!DOCTYPE html>
<html lang="en">
<head>
<meta charset="utf-8">
<title>dottyfaze baking co. – 1-Pack Dieline</title>
<link href="https://fonts.googleapis.com/css2?family=Quicksand:wght@600&family=Open+Sans:wght@400;700&family=Luckiest+Guy&display=swap" rel="stylesheet">
<style>
  :root {
    --paper: #ffffff;
    --cream: #fdf0cc;
    --gingham-a: #fbd27a;
    --gingham-b: #fde7b2;
    --brand-brown: #b98346;
    --ink-brown: #5b2a1c;
    --cut-line: #1a1a1a;
    --bleed-green: #49b649;
    --dim-blue: #3553a8;
    --dim-grey: #8a8a8a;
    --title-yellow: #f7c531;
    --photo-yellow: #f2c21c;
    --photo-red: #d9262c;
  }
  * { box-sizing: border-box; margin: 0; padding: 0; }
  html, body { width: 1200px; height: 850px; overflow: hidden; background: var(--paper); }
  .canvas { position: relative; width: 1200px; height: 850px; }
  .dieline { position: absolute; inset: 0; }
  .panel { position: absolute; }
  .gingham {
    background: linear-gradient(135deg, var(--gingham-a), var(--gingham-b) 50%, var(--gingham-a));
  }
  .cream { background: var(--cream); }
  .brand {
    font-family: "Quicksand", sans-serif;
    font-weight: 600;
    color: var(--brand-brown);
    display: flex;
    align-items: center;
    gap: 6px;
    white-space: nowrap;
    line-height: 1;
  }
  .brand-dot { width: 0.7em; height: 0.7em; border-radius: 50%; background: var(--brand-brown); flex: none; }
  .brand-vertical {
    position: absolute;
    transform: translate(-50%, -50%) rotate(90deg);
    font-size: 28px;
  }
  .recipe-card {
    position: absolute;
    left: 204px; top: 314px; width: 366px; height: 380px;
    overflow: hidden;
    background: linear-gradient(160deg, #f7f5f2, #ffffff 45%, #efe7e2);
    border: 2px solid #c9a48a;
    padding: 6px 12px;
    font-family: "Open Sans", sans-serif;
    color: var(--ink-brown);
    font-size: 8.4px;
    line-height: 1.24;
  }
  .recipe-card .brand { justify-content: center; font-size: 15px; margin-bottom: 3px; }
  .recipe-card h3 {
    font-size: 9px; font-weight: 700; text-align: center;
    border-top: 1px solid var(--ink-brown); margin-top: 3px; padding-top: 2px;
  }
  .ingredients { display: grid; grid-template-columns: 1fr 0.8fr; }
  .instructions { list-style: none; padding-left: 24px; }
  .cleaning { text-align: center; }
  .product-window {
    position: absolute;
    left: 734px; top: 338px; width: 326px; height: 326px;
    border: 2px solid #222;
    background:
      linear-gradient(to bottom, transparent 70%, rgba(217, 38, 44, 0.75) 70%),
      radial-gradient(circle at 50% 40%, #f8d24a, var(--photo-yellow) 60%, #d9a514);
  }
  .product-title {
    position: absolute;
    left: 689px; width: 437px; top: 672px;
    text-align: center;
    font-family: "Luckiest Guy", sans-serif;
    font-size: 20px;
    letter-spacing: 0.5px;
    color: var(--title-yellow);
    -webkit-text-stroke: 1.2px var(--ink-brown);
  }
  .dim-label { font-family: "Open Sans", sans-serif; font-size: 13px; fill: var(--dim-blue); }
  .dim-label.muted { fill: var(--dim-grey); font-size: 14px; }
</style>
</head>
<body>
<div class="canvas">

  <svg class="dieline" width="1200" height="850" viewBox="0 0 1200 850">
    <defs>
      <path id="cut-path" d="M72,288 L72,240 L84,228 L156,228 L176,262 L176,200 L188,190 L188,46 L584,46 L584,190 L596,200 L596,262 L616,228 L676,228 L689,240 L689,196 L702,186 L718,124 Q728,104 752,104 L1062,104 Q1086,104 1096,124 L1112,186 L1126,196 L1126,288 L1160,298 L1182,306 L1182,692 L1160,700 L1126,708 L1126,800 L1108,820 L708,820 L689,800 L689,708 L676,708 L676,760 L612,760 L596,744 L596,820 L176,820 L176,744 L160,760 L90,760 L72,744 Z"/>
    </defs>
    <use href="#cut-path" fill="none" stroke="var(--bleed-green)" stroke-width="20" stroke-linejoin="round"/>
    <use href="#cut-path" fill="var(--paper)" stroke="var(--paper)" stroke-width="17" stroke-linejoin="round"/>
  </svg>

  <div class="panel gingham" role="img" aria-label="Yellow gingham pattern" style="left:188px; top:46px; width:396px; height:242px;"></div>
  <div class="panel cream" style="left:689px; top:198px; width:437px; height:90px;">
    <div class="brand" style="justify-content:center; font-size:30px; margin-top:28px;"><span class="brand-dot"></span>dottyfaze baking co.</div>
  </div>

  <div class="panel cream" style="left:72px; top:288px; width:104px; height:420px;"></div>
  <div class="panel gingham" role="img" aria-label="Yellow gingham pattern" style="left:176px; top:288px; width:420px; height:420px;"></div>
  <div class="panel cream" style="left:596px; top:288px; width:93px; height:420px;"></div>
  <div class="panel gingham" role="img" aria-label="Yellow gingham pattern" style="left:689px; top:288px; width:437px; height:420px;"></div>

  <div class="brand brand-vertical" style="left:124px; top:498px;"><span class="brand-dot"></span>dottyfaze baking co.</div>
  <div class="brand brand-vertical" style="left:642px; top:498px;"><span class="brand-dot"></span>dottyfaze baking co.</div>

  <section class="recipe-card">
    <div class="brand"><span class="brand-dot"></span>dottyfaze baking co.</div>
    <p>Thank you for purchasing an emoji cookie cutter! We thought we would share our TOP SECRET recipe for dottyfaze sugar cookie success. See below for ingredients and instructions:</p>
    <h3>Ingredients:</h3>
    <div class="ingredients">
      <span>3 cups of unbleached all-purpose flour</span><span>1 cup of sugar</span>
      <span>2 tsp baking powder</span><span>1 egg</span>
      <span>2 sticks of salted butter, cold</span><span>1¼ tsp of vanilla extract</span>
    </div>
    <h3>Instructions:</h3>
    <ul class="instructions">
      <li>Preheat oven to 350 degrees</li>
      <li>Combine the flour and baking powder, set aside</li>
      <li>Cut cold butter into small chunks and mix it with the sugar until creamy</li>
      <li>Add the egg and vanilla extract to the sugar and butter mixture</li>
      <li>Slowly add in the flour mixture until fully combined (scrape the bowl to mix all the flour in)</li>
      <li>Roll out onto a floured mat (we recommend also flouring the rolling pin and cookie cutter)</li>
      <li>Make sure the dough is no less than ¼ inch thick</li>
      <li>Press the dottyfaze cutter firmly into the dough</li>
      <li>Transfer your cutouts to a parchment paper lined baking sheet</li>
      <li>Tip: put your cutouts in the freezer for 3 minutes before baking, this helps maintain shape</li>
      <li>Bake for 10 minutes, or until edges are very light brown</li>
      <li>Let cool for an hour before icing, then use your favorite icing recipe to trace the lines!</li>
    </ul>
    <h3>Cleaning:</h3>
    <p class="cleaning">Our dottyfaze cutters are made of environmentally friendly, organic, biodegradable materials and must be hand washed in slightly warm water using antibacterial dish washing soap. Do not put in dishwasher.</p>
  </section>

  <div class="brand" style="position:absolute; left:689px; width:437px; top:298px; justify-content:center; font-size:22px;"><span class="brand-dot"></span>dottyfaze baking co.</div>
  <div class="product-window" role="img" aria-label="Photo of iced yellow emoji sugar cookies with red plastic cookie cutters in front"></div>
  <div class="product-title">Smile Face Cookie Cutter</div>

  <svg class="dieline" width="1200" height="850" viewBox="0 0 1200 850">
    <use href="#cut-path" fill="none" stroke="var(--cut-line)" stroke-width="1.4" stroke-linejoin="round"/>
    <g stroke="var(--cut-line)" stroke-width="1.2" fill="none">
      <line x1="176" y1="288" x2="176" y2="708"/>
      <line x1="596" y1="288" x2="596" y2="708"/>
      <line x1="689" y1="288" x2="689" y2="708"/>
      <line x1="1126" y1="288" x2="1126" y2="708"/>
      <path d="M360,104 L360,120 Q360,136 376,136 L380,136 Q386,160 400,162 Q414,160 420,136 L424,136 Q440,136 440,120 L440,104 Z" fill="var(--paper)"/>
    </g>
    <g stroke="var(--dim-blue)" stroke-width="1" fill="none">
      <line x1="145" y1="74" x2="145" y2="190"/><line x1="136" y1="74" x2="154" y2="74"/><line x1="136" y1="190" x2="154" y2="190"/>
      <line x1="55" y1="202" x2="55" y2="286"/><line x1="46" y1="202" x2="64" y2="202"/><line x1="46" y1="286" x2="64" y2="286"/>
      <line x1="55" y1="292" x2="55" y2="706"/><line x1="46" y1="292" x2="64" y2="292"/><line x1="46" y1="706" x2="64" y2="706"/>
      <line x1="178" y1="812" x2="594" y2="812"/><line x1="178" y1="804" x2="178" y2="820"/><line x1="594" y1="804" x2="594" y2="820"/>
      <line x1="1164" y1="116" x2="1164" y2="196"/><line x1="1155" y1="116" x2="1173" y2="116"/><line x1="1155" y1="196" x2="1173" y2="196"/>
    </g>
    <text class="dim-label" transform="translate(134 132) rotate(-90)" text-anchor="middle">1 in</text>
    <text class="dim-label" transform="translate(46 244) rotate(-90)" text-anchor="middle">0.813 in</text>
    <text class="dim-label muted" transform="translate(46 498) rotate(-90)" text-anchor="middle">(D) 3.875 in</text>
    <text class="dim-label muted" x="386" y="806" text-anchor="middle">(L) 3.875 in</text>
    <text class="dim-label" x="616" y="814" style="font-size:10px; fill:var(--dim-grey);">(D) 0.875 in</text>
    <text class="dim-label" x="1122" y="161" style="font-size:15px;">0.781 in</text>
    <text class="dim-label" x="900" y="814" text-anchor="middle" style="font-size:15px;">3</text>
  </svg>

</div>
</body>
</html>
```